Marketing Flyer for Plumber Referals

8.5" x11" Layout should be landscape not portrait. Create a bold, eye-catching flyer that highlights earning potential from referrals for water damage restoration. Use high-contrast colors like blue, yellow, and white, with bold fonts and dynamic layouts. Include images of restoration work, cash, and happy clients. Emphasize key benefits like $500 minimum payouts, fast payments, and unlimited income potential. Keep instructions simple: refer a client, we handle the work, you get paid. Add a clear call-to-action and display contact details prominently. Focus on professionalism and energy.

Target Market(s)

Plumbers and Contractor 8.5" x11" Layout should be landscape not portrait.

Industry/Entity Type

General Contractor

Colors
0054AA
0677BA
7BADD7
CADEEF
E8F1F8
EB3D1F
EC4F4E
F09395
F8D3D4
FCEDEE

Requirements
Must have
• 8.5" x11" Layout should be landscape not portrait.
Nice to have

```html
<!DOCTYPE html>
<html lang="en">
<head>
<meta charset="utf-8">
<title>Referral Flyer – Coastline Remodel</title>
<link href="https://fonts.googleapis.com/css2?family=Poppins:wght@300;400;500;600;700;800&family=Roboto+Condensed:wght@400&display=swap" rel="stylesheet">
<style>
  :root{
    --blue:#0054AA;
    --blue-mid:#0677BA;
    --blue-soft:#7BADD7;
    --blue-pale:#CADEEF;
    --blue-mist:#E8F1F8;
    --red:#EB3D1F;
    --ink:#111111;
    --logo-bg:#1b1b1b;
    --white:#ffffff;
  }
  *{margin:0;padding:0;box-sizing:border-box}
  html,body{width:1200px;height:961px;overflow:hidden;background:var(--white)}
  body{position:relative;font-family:'Poppins',sans-serif;color:var(--ink)}
  .page-label{position:absolute;left:70px;top:42px;font-size:15px;color:#555;font-weight:400}
  .flyer{position:absolute;left:72px;top:72px;width:1057px;height:817px;background:var(--blue-mist);overflow:hidden}
  .abs{position:absolute}

  /* hero */
  .hero-cash{left:0;top:0;width:529px;height:348px;background:linear-gradient(135deg,#2b3440 0%,#1d2530 45%,#2f3a3f 100%)}
  .hero-red{left:529px;top:0;width:528px;height:348px;background:var(--red)}
  .hand-photo{left:858px;top:146px;width:182px;height:202px;border-radius:90px 60px 0 0;background:linear-gradient(160deg,#f1c8ad 0%,#e0a888 60%,#d99a7c 100%);opacity:.9}
  .brand-box{left:427px;top:19px;width:204px;height:151px;background:var(--logo-bg);display:flex;align-items:center;justify-content:center;gap:8px}
  .brand-box .dot{width:10px;height:10px;background:var(--white)}
  .brand-box .brand-name{color:var(--white);font-size:17px;font-weight:400;letter-spacing:.5px}
  .referrals-word{left:652px;top:88px;font-size:62px;font-weight:300;color:var(--white);letter-spacing:1px;line-height:1}
  .underline{left:652px;top:150px}
  .hero-left-text{right:528px;top:200px;text-align:right;color:var(--white);line-height:42px;font-size:47px}
  .hero-right-text{left:548px;top:200px;color:var(--white);line-height:42px;font-size:47px}
  .thin{font-weight:400}
  .heavy{font-weight:800}

  /* strip */
  .strip{left:0;top:348px;width:1057px;height:33px;background:var(--blue-pale)}
  .strip-left{left:0;width:529px;top:5px;text-align:center;font-size:15px;color:var(--blue);padding-left:70px}
  .strip-left b{font-weight:700}
  .strip-right{left:550px;top:1px;font-size:22px;color:var(--blue)}
  .strip-right .red{color:var(--red)}
  .strip-right .ink{color:var(--ink)}
  .strip-right b{font-weight:700}

  /* photos */
  .photo-flood{left:0;top:381px;width:316px;height:173px;background:linear-gradient(180deg,#cfd4d6 0%,#8a9296 45%,#3d4245 100%)}
  .photo-pipe{left:0;top:554px;width:316px;height:178px;background:linear-gradient(90deg,#5a5f63 0%,#a9adb0 45%,#e6e7e8 70%,#8c9194 100%)}

  /* benefits */
  .why{left:316px;top:416px;width:741px;text-align:center;font-size:22px;font-weight:700;color:var(--blue)}
  .why span{color:var(--red)}
  .divider{width:1px;background:#333;top:465px;height:176px}
  .benefit{top:463px;width:170px;text-align:center;margin-left:-85px}
  .benefit .icon{width:74px;height:74px;border-radius:50%;margin:0 auto 20px;display:flex;align-items:center;justify-content:center}
  .benefit h3{font-size:19px;line-height:20px;font-weight:700}
  .benefit p{font-family:'Roboto Condensed',sans-serif;font-size:14px;line-height:16px;margin-top:6px;color:var(--ink)}
  .is-blue .icon{background:var(--blue)} .is-blue h3{color:var(--blue)}
  .is-red .icon{background:var(--red)} .is-red h3{color:var(--red)}
  .slogan{left:316px;top:670px;width:741px;text-align:center;font-size:24px;font-weight:700;color:var(--blue);padding-left:10px}
  .slogan span{color:var(--red)}

  /* contact */
  .accent-bar{left:-1px;top:734px;width:528px;height:5px;background:var(--blue)}
  .contact{left:0;top:739px;width:1057px;height:78px;background:var(--blue-pale)}
  .contact-cta{left:27px;top:28px;font-size:23px;font-weight:700}
  .contact-sep{top:16px;width:1px;height:46px;background:#333}
  .contact-phone{left:329px;top:2px;font-size:48px;font-weight:700;letter-spacing:1px}
  .contact-web{left:696px;top:28px;font-size:23px;font-weight:700}
</style>
</head>
<body>
<div class="page-label">Front Page</div>

<main class="flyer">
  <div class="abs hero-cash" role="img" aria-label="Photo of scattered hundred-dollar bills with letter tiles spelling cash flow"></div>
  <div class="abs hero-red"></div>
  <div class="abs hand-photo" role="img" aria-label="Photo of a hand holding a white marker"></div>

  <div class="abs brand-box"><span class="dot"></span><span class="brand-name">COASTLINE REMODEL</span></div>

  <div class="abs referrals-word">REFERRALS</div>
  <svg class="abs underline" width="360" height="30" viewBox="0 0 360 30"><path d="M2 24 C90 14 200 10 340 14" stroke="#fff" stroke-width="5" fill="none" stroke-linecap="round"/></svg>

  <div class="abs hero-left-text"><div class="thin">EARN</div><div class="heavy">UNLIMITED</div><div class="heavy">CASH</div></div>
  <div class="abs hero-right-text"><div class="thin">GET PAID TO</div><div class="heavy">REFER A</div><div class="heavy">FLOOD</div></div>

  <section class="abs strip">
    <div class="abs strip-left">Partner with the <b>#1 Water Damage Restoration Team</b></div>
    <div class="abs strip-right"><span class="red"><b>$500</b> Minimum</span> <span class="ink">or</span> <b>10%</b> Per Referral!</div>
  </section>

  <div class="abs photo-flood" role="img" aria-label="Photo of a flooded room with a staircase"></div>
  <div class="abs photo-pipe" role="img" aria-label="Photo of a leaking white drain pipe"></div>

  <h2 class="abs why">Why Partner with <span>Us?</span></h2>

  <div class="abs divider" style="left:513px"></div>
  <div class="abs divider" style="left:691px"></div>
  <div class="abs divider" style="left:849px"></div>

  <div class="abs benefit is-blue" style="left:423px">
    <div class="icon"><svg width="40" height="40" viewBox="0 0 40 40" fill="none" stroke="#fff" stroke-width="2.2"><circle cx="20" cy="20" r="14"/><path d="M24 14h-6a3 3 0 0 0 0 6h4a3 3 0 0 1 0 6h-6M20 10v20"/></svg></div>
    <h3>Guaranteed<br>Payout</h3>
    <p>Minimum $500 or 10% of the invoice, paid fast.</p>
  </div>
  <div class="abs benefit is-red" style="left:601px">
    <div class="icon"><svg width="40" height="40" viewBox="0 0 40 40" fill="none" stroke="#fff" stroke-width="2.2"><rect x="8" y="6" width="20" height="26" rx="2"/><circle cx="19" cy="19" r="6"/><path d="M16 19l2 2 4-4M23 24l8 8"/></svg></div>
    <h3>Free<br>Evaluations</h3>
    <p>We assess damage and process insurance claims for your clients.</p>
  </div>
  <div class="abs benefit is-blue" style="left:774px">
    <div class="icon"><svg width="40" height="40" viewBox="0 0 40 40" fill="none" stroke="#fff" stroke-width="2.2"><circle cx="20" cy="13" r="6"/><path d="M8 34c0-8 5-12 12-12s12 4 12 12z"/></svg></div>
    <h3>Industry<br>Leaders</h3>
    <p>Certified experts with 24/7 rapid response.</p>
  </div>
  <div class="abs benefit is-red" style="left:944px">
    <div class="icon"><svg width="40" height="40" viewBox="0 0 40 40" fill="none" stroke="#fff" stroke-width="2.2"><path d="M10 12h7a3 3 0 1 1 6 0h7v7a3 3 0 1 1 0 6v7H10v-7a3 3 0 1 0 0-6z"/></svg></div>
    <h3>Affordable<br>Solutions</h3>
    <p>Lowest out-of-pocket costs for your customers.</p>
  </div>

  <p class="abs slogan">Send Referrals. <span>Get Paid.</span> Grow Your Business.</p>

  <div class="abs accent-bar"></div>
  <footer class="abs contact">
    <div class="abs contact-cta">Call Text or Book on-line</div>
    <div class="abs contact-sep" style="left:319px"></div>
    <div class="abs contact-phone">858-555-0147</div>
    <div class="abs contact-sep" style="left:686px"></div>
    <div class="abs contact-web">ShorelineRebuild.com</div>
  </footer>
</main>
</body>
</html>
```